Broschüre für Kommunikationswissenschaftler
Zielgruppe
Ich bin Kommunikationswissenschaftler und halte Vorträge für und vor Unternehmen. Meine Zielgruppe sind Menschen, die an Leadership und Persönlichkeitsentwicklung interessiert sind. Vorwiegend Vertrieb über Eventagenturen und Entscheider auf C-Level Ebene.
Aufgabenstellung
Benötigt wird ein neues Design für meine Broschüre anbei.
Logo und Inhalte sind gesetzt.
Farbgebung mit Orientierung an der Website www.Tobiwendler.de
Gerne mit Chinesischen Ornamenten - hochwertig, statt zu verspielt.

```html
<!DOCTYPE html>
<html lang="de">
<head>
<meta charset="utf-8">
<title>Faustregeln der Selbstdisziplin – Broschüre</title>
<link href="https://fonts.googleapis.com/css2?family=Montserrat:ital,wght@0,300;0,400;0,600;0,700;1,300;1,700&family=Noto+Serif+SC:wght@400;700&display=swap" rel="stylesheet">
<style>
:root{
  --slate:#2f3944;
  --slate-deep:#262e37;
  --slate-soft:#3a4550;
  --blue:#1d55b8;
  --blue-soft:#5a86d1;
  --paper:#f7f8f9;
  --stage-top:#dcdde0;
  --stage-low:#f1f1f2;
  --ink:#2b2f35;
  --grey:#7d838a;
  --han-faint:#d4d8de;
}
*{margin:0;padding:0;box-sizing:border-box}
html,body{width:1200px;height:3245px;overflow:hidden}
body{
  position:relative;
  font-family:"Montserrat",sans-serif;
  color:var(--ink);
  background:linear-gradient(to bottom,var(--stage-top) 0,#e7e8ea 1467px,var(--stage-low) 1467px);
}
.abs{position:absolute}

/* ---------- cover ---------- */
.cover{position:absolute;background:var(--slate);overflow:hidden;color:#fff}
.cover-strip{position:absolute;top:0;right:0;bottom:0;background:var(--blue);display:flex;flex-direction:column;align-items:center;justify-content:space-around;padding:20px 0}
.cover-strip span{font-family:"Noto Serif SC",serif;color:var(--blue-soft);font-size:28px;line-height:1}
.brand{display:flex;align-items:center;gap:10px}
.brand-dot{width:18px;height:18px;border-radius:50%;background:#fff;flex:none}
.brand-name{font-weight:600;font-size:15px;letter-spacing:.5px;line-height:1.1}
.brand-sub{font-weight:300;font-size:9px;letter-spacing:2px;display:block}
.cover-title{font-weight:700;font-size:30px;line-height:1.15}
.cover-rule{height:4px;background:var(--blue);width:150px}
.dragon{position:absolute;background:radial-gradient(ellipse at center,rgba(255,255,255,.07),rgba(255,255,255,0) 70%)}

.back h2{font-weight:700;font-style:italic;font-size:26px;line-height:1}
.back .sub{font-weight:300;font-style:italic;font-size:18px}
.back p{font-size:8.5px;line-height:1.6;font-style:italic;color:#c6ccd3}
.back .wish{font-weight:700;font-style:italic;color:#fff;font-size:8.5px}
.signature{background:linear-gradient(90deg,rgba(255,255,255,.25),rgba(255,255,255,.05))}
.url{font-size:13px;letter-spacing:1px;font-weight:300;color:#c6ccd3}

/* ---------- spreads ---------- */
.spread{position:absolute;width:480px;height:343px;display:flex;box-shadow:0 10px 18px rgba(0,0,0,.12)}
.page{position:relative;width:240px;height:100%;background:var(--paper);overflow:hidden}
.page+.page{box-shadow:inset 6px 0 8px -6px rgba(0,0,0,.12)}
.page.dark{background:var(--slate)}

.rule{position:absolute;width:214px}
.rule-han{position:absolute;left:0;top:-4px;font-family:"Noto Serif SC",serif;font-size:24px;color:var(--ink);line-height:1}
.rule-num{position:absolute;left:30px;top:4px;font-size:26px;font-weight:300;color:var(--grey);line-height:1}
.rule-head{margin-left:62px}
.rule-lead{font-size:8px;color:var(--blue);line-height:1.2}
.rule-title{font-size:11px;font-weight:700;color:var(--blue);line-height:1.2;text-transform:uppercase}
.rule-text{margin-left:62px;margin-top:10px}
.rule-text p{font-size:5.4px;line-height:1.7;color:var(--grey);margin-bottom:6px}
.rule-text p.note{color:var(--blue);font-weight:700}

.quote{color:#dfe3e8;font-size:15px;font-weight:300;line-height:1.2}
.quote b{font-size:21px;font-weight:700;color:#fff;display:block}
.tiny{font-size:6px;color:#9aa2ab;line-height:1.5}
.photo{background:linear-gradient(160deg,#5b636b,#2a3036)}
.photo.bw{background:linear-gradient(160deg,#8a8f94,#1f2327)}
.corner{position:absolute;border-color:var(--blue);border-style:solid;border-width:0}
.han-col{position:absolute;display:flex;flex-direction:column;align-items:center;gap:4px;font-family:"Noto Serif SC",serif;color:var(--han-faint);font-size:22px;line-height:1}
.han-row{position:absolute;font-family:"Noto Serif SC",serif;color:var(--han-faint);font-size:26px;letter-spacing:8px}
.label{font-size:8px;color:#fff;text-transform:uppercase;letter-spacing:.3px}
.label b{display:block;font-weight:700}
.body-dark p{font-size:5.4px;line-height:1.7;color:#aab2bb;margin-bottom:6px}
.claim{font-size:9px;line-height:1.3;color:var(--ink)}
.claim b{font-size:12px;font-weight:700;display:block;text-transform:uppercase}
.sec-title{font-size:11px;font-weight:700;color:var(--blue);text-transform:uppercase}
.note-line{position:absolute;left:24px;right:24px;height:1px;background:var(--blue)}
.check{display:flex;gap:4px;align-items:flex-start;font-size:5px;color:#aab2bb;line-height:1.5;margin-bottom:5px}
.check svg{flex:none;margin-top:1px}

.logo-sheet{position:absolute;display:flex;flex-direction:column;align-items:center;gap:10px}
.logo-name{font-size:44px;font-weight:400;letter-spacing:1px;color:var(--ink)}
.logo-sub{font-size:20px;font-weight:400;letter-spacing:9px;color:var(--ink)}
.logo-dot{width:46px;height:46px;border-radius:50%;background:var(--ink)}
</style>
</head>
<body>

<!-- ===== Front cover ===== -->
<section class="cover" style="left:420px;top:110px;width:360px;height:510px">
  <div class="cover-strip" style="width:64px">
    <span>少</span><span>林</span><span>家</span><span>拳</span><span>少</span><span>林</span><span>家</span><span>拳</span>
  </div>
  <div class="brand abs" style="left:34px;top:44px">
    <span class="brand-dot"></span>
    <span class="brand-name">TOBI WENDLER<span class="brand-sub">KEYNOTE SPEAKER</span></span>
  </div>
  <h1 class="cover-title abs" style="left:34px;top:130px">Faustregeln der<br>Selbstdisziplin</h1>
  <div class="cover-rule abs" style="left:34px;top:222px"></div>
  <div class="dragon" role="img" aria-label="Feine chinesische Drachenzeichnung" style="left:80px;top:270px;width:220px;height:230px"></div>
</section>

<!-- ===== Open cover spread ===== -->
<section class="cover back" style="left:200px;top:840px;width:400px;height:540px;background:var(--slate-deep)">
  <div class="abs" style="left:40px;top:46px">
    <h2>ZIELE</h2>
    <div class="sub">erreichen</div>
    <div class="sub" style="margin-top:14px">mit durchschlagendem</div>
    <h2 style="font-size:22px">ERFOLG!</h2>
  </div>
  <div class="abs" style="left:40px;top:200px;width:300px">
    <p>Dieses Kompendium hilft Ihnen beim Erinnern und Dranbleiben. Haben Sie es dabei, schauen Sie immer wieder hinein, machen Sie es zu Ihrem Begleiter.</p>
    <p style="margin-top:10px">Dann wird es Ihnen gelingen, Stress in positive und produktive Energie umzuwandeln und Ihre Ziele zu erreichen.</p>
    <p style="margin-top:10px">Der Schlüssel zu langfristigem Erfolg ist nicht von einem speziellen Vertriebsziel oder einem Projekt- oder Businessplan abhängig, sondern von Ihrer mentalen Stärke!</p>
    <p class="wish" style="margin-top:14px">Ich wünsche Ihnen von ganzem Herzen viel Erfolg!</p>
  </div>
  <div class="signature abs" role="img" aria-label="Handschriftliche Unterschrift" style="left:40px;top:392px;width:110px;height:26px"></div>
  <p class="abs" style="left:40px;top:428px;font-size:8.5px;font-style:italic;color:#c6ccd3;line-height:1.5">Ihr<br>Tobi Wendler</p>
  <div class="url abs" style="left:40px;top:482px">WWW.TOBIWENDLER.DE</div>
  <div class="cover-rule abs" style="left:40px;top:504px;width:80px;height:3px"></div>
</section>
<section class="cover" style="left:600px;top:840px;width:400px;height:540px">
  <div class="cover-strip" style="width:70px">
    <span>少</span><span>林</span><span>家</span><span>拳</span><span>少</span><span>林</span><span>家</span><span>拳</span>
  </div>
  <div class="brand abs" style="left:36px;top:48px">
    <span class="brand-dot"></span>
    <span class="brand-name">TOBI WENDLER<span class="brand-sub">KEYNOTE SPEAKER</span></span>
  </div>
  <h1 class="cover-title abs" style="left:36px;top:136px">Faustregeln der<br>Selbstdisziplin</h1>
  <div class="cover-rule abs" style="left:36px;top:228px"></div>
  <div class="dragon" role="img" aria-label="Feine chinesische Drachenzeichnung" style="left:-60px;top:280px;width:300px;height:250px"></div>
</section>

<!-- ===== Row 1 ===== -->
<section class="spread" style="left:59px;top:1533px">
  <div class="page dark">
    <div class="quote abs" style="left:34px;top:90px">Nicht das<b>ANFANGEN</b>wird belohnt,<br><br>sondern das<b>DURCHHALTEN!</b></div>
    <div class="tiny abs" style="left:34px;top:270px">Tobi Wendler<br>Der stille Kranich</div>
  </div>
  <div class="page">
    <div class="abs" style="left:0;top:0;width:12px;height:100%;background:var(--slate)"></div>
    <div class="photo abs" role="img" aria-label="Porträtfoto des Redners" style="left:-60px;top:40px;width:262px;height:262px"></div>
    <div class="corner" style="left:120px;top:26px;width:90px;height:40px;border-top-width:3px;border-right-width:3px"></div>
    <div class="abs" style="left:14px;top:314px;width:110px;height:3px;background:var(--blue)"></div>
  </div>
</section>

<section class="spread" style="left:646px;top:1533px">
  <div class="page">
    <div class="rule" style="left:14px;top:22px">
      <span class="rule-han">六</span><span class="rule-num">6.</span>
      <div class="rule-head"><p class="rule-lead">Schlucken Sie notfalls auch mal</p><h3 class="rule-title">die bittere Pille!</h3></div>
      <div class="rule-text"><p>Schlucken Sie die Kröte früh am Tag. Erledigen Sie zuerst das, was Sie am liebsten aufschieben würden. Danach fällt Ihnen der Rest viel leichter.</p><p class="note">Sobald die Kröte geschluckt ist, wird der Rest des Tages leichter.</p></div>
    </div>
    <div class="rule" style="left:14px;top:188px">
      <span class="rule-han">七</span><span class="rule-num">7.</span>
      <div class="rule-head"><p class="rule-lead">Nutzen Sie die Kraft der</p><h3 class="rule-title">Selbstverpflichtung!</h3></div>
      <div class="rule-text"><p>Erzählen Sie Ihrem Umfeld von Ihren Vorhaben. So wächst der Druck, auch dranzubleiben, und Sie erhalten ehrliches Feedback.</p></div>
    </div>
  </div>
  <div class="page">
    <div class="rule" style="left:10px;top:22px">
      <span class="rule-han">八</span><span class="rule-num">8.</span>
      <div class="rule-head"><p class="rule-lead">Schieben Sie die</p><h3 class="rule-title">Belohnung auf!</h3></div>
      <div class="rule-text"><p>Belohnen Sie sich nicht jedes Mal, wenn Sie es verdient haben. Belohnung bleibt nur wirksam, wenn sie selten kommt. So trainieren Sie Ihren Willen wie einen Muskel.</p></div>
    </div>
    <div class="rule" style="left:10px;top:160px">
      <span class="rule-han">九</span><span class="rule-num">9.</span>
      <div class="rule-head"><p class="rule-lead">Helfen Sie anderen beim</p><h3 class="rule-title">Ziele erreichen!</h3></div>
      <div class="rule-text"><p>Unterstützen Sie andere dabei, ihre Ziele zu erreichen. Wer anderen hilft, bringt Ordnung in das eigene Denken und lernt dabei selbst am meisten.</p><p class="note">Eine chinesische Weisheit sagt: Durch Lehren lernen wir.</p></div>
    </div>
  </div>
</section>

<!-- ===== Row 2 ===== -->
<section class="spread" style="left:59px;top:1958px;height:340px">
  <div class="page">
    <div class="abs" style="left:0;top:0;width:240px;height:26px;background:var(--blue);color:#fff;font-size:10px;font-weight:600;text-align:center;line-height:26px">TOBI WENDLER</div>
    <div class="han-col" style="left:10px;top:44px"><span>愉</span><span>快</span><span>的</span><span>春</span><span>節</span></div>
    <div class="photo bw abs" role="img" aria-label="Schwarzweiß-Porträt des Redners" style="left:68px;top:26px;width:172px;height:206px"></div>
    <div class="abs" style="left:0;top:232px;width:96px;height:108px;background:var(--blue)"></div>
    <div class="abs" style="left:112px;top:248px;font-size:10px;line-height:1.3">
      <b style="display:block;font-size:11px">DISZIPLIN</b><span style="font-size:7px">IST NICHT KÄUFLICH,</span><br><br>
      <span style="font-size:7px">ABER SIE</span><b style="display:block;font-size:9px">ZAHLT SICH AUS!</b>
    </div>
  </div>
  <div class="page">
    <div class="abs dark body-dark" style="left:0;top:0;width:240px;height:232px;background:var(--slate);padding:64px 24px 0">
      <div class="label" style="margin-bottom:14px">Der stille Kranich</div>
      <p>Tobi Wendler verbrachte einen großen Teil seines Lebens in verschiedenen Kulturen und lernte bei Meistern die asiatische Kampfkunst.</p>
      <p>Heute besitzt er schwarze Gürtel in mehreren Stilen.</p>
      <p>Er studierte Kommunikation und interkulturelle Zusammenarbeit.</p>
      <p>Sein Geheimnis sind die Lehren alter Meister.</p>
    </div>
    <div class="abs" style="left:36px;top:250px;width:186px;height:2px;background:var(--blue)"></div>
    <div class="han-row" style="left:36px;top:272px">愉快的春節</div>
  </div>
</section>

<section class="spread" style="left:646px;top:1958px;height:350px">
  <div class="page">
    <div class="rule" style="left:14px;top:22px">
      <span class="rule-han">十</span><span class="rule-num">10.</span>
      <div class="rule-head"><p class="rule-lead">Brechen Sie</p><h3 class="rule-title">die Regeln!</h3></div>
      <div class="rule-text"><p>Folgen Sie nicht blind jeder Regel.</p><p>Vertrauen Sie auf sich selbst und prüfen Sie, welche Regeln Ihnen dienen. Dann stellen Sie eigene Regeln auf.</p><p class="note">Brechen Sie die Regeln, aber nicht das Gesetz.</p></div>
    </div>
    <div class="abs" style="left:130px;top:220px;width:110px;height:130px;background:var(--blue)"></div>
  </div>
  <div class="page">
    <div class="abs" style="left:0;top:0;width:240px;height:28px;background:var(--blue)"></div>
    <div class="abs" style="left:0;top:220px;width:100px;height:130px;background:var(--blue)"></div>
    <div class="han-col" style="left:12px;top:44px"><span>愉</span><span>快</span><span>的</span><span>春</span><span>節</span></div>
    <div class="abs body-dark" style="left:70px;top:28px;width:170px;height:192px;background:var(--slate);padding:30px 14px 0">
      <div class="label" style="margin-bottom:14px;font-size:7px">Das Wichtigste:<b style="font-weight:400">Vermeiden Sie den Selbstbetrug</b></div>
      <p>Sie müssen es nicht der ganzen Welt erzählen, wenn Sie eigene Erwartungen nicht erfüllen. Seien Sie aber ehrlich zu sich selbst.</p>
      <p>Nur wenn Sie sich mit kleinen Schritten belügen, rückt Ihr Erfolg in weite Ferne.</p>
    </div>
    <div class="claim abs" style="left:112px;top:246px">Wenn Sie sich selbst<b>betrügen,</b><span style="display:block;margin-top:8px">Werden Sie nicht</span><b>erfolgreich</b>sein!</div>
  </div>
</section>

<!-- ===== Row 3 ===== -->
<section class="spread" style="left:59px;top:2388px">
  <div class="page">
    <div class="rule" style="left:8px;top:24px">
      <span class="rule-han">一</span><span class="rule-num">1.</span>
      <div class="rule-head"><p class="rule-lead">Hören Sie auf zu</p><h3 class="rule-title">Jammern!</h3></div>
      <div class="rule-text"><p>Durch Jammern ist noch nie etwas besser geworden. Jammern vermehrt das Leid und kostet Kraft.</p><p class="note">Hören Sie auf zu jammern und gewinnen Sie Willenskraft für wichtige Dinge.</p></div>
    </div>
    <div class="rule" style="left:8px;top:178px">
      <span class="rule-han">二</span><span class="rule-num">2.</span>
      <div class="rule-head"><p class="rule-lead">Etablieren Sie</p><h3 class="rule-title">Rituale!</h3></div>
      <div class="rule-text"><p>Feste Abläufe sparen Entscheidungen. Was zur Gewohnheit wird, kostet keine Willenskraft mehr.</p><p class="note">Rituale tragen Sie durch schwierige Tage.</p></div>
    </div>
  </div>
  <div class="page">
    <div class="rule" style="left:10px;top:24px">
      <span class="rule-han">三</span><span class="rule-num">3.</span>
      <div class="rule-head"><p class="rule-lead">Lernen Sie von</p><h3 class="rule-title">den Besten!</h3></div>
      <div class="rule-text"><p>Tun Sie, was Ihr Vorbild tut, und Sie kommen zum Ziel. Lernen Sie von denen, die Sie bewundern.</p><p>Sie wollen unbesiegbar sein? Nehmen Sie einen Kämpfer zum Vorbild.</p><p>Sie wollen schön und begehrenswert sein? Nehmen Sie eine Ikone zum Vorbild.</p><p>Sie wollen den höchsten Gipfel erklimmen? Folgen Sie einem Bergsteiger.</p><p class="note">Vorbilder sind Quellen der Inspiration und Wertevermittler.</p></div>
    </div>
  </div>
</section>

<section class="spread" style="left:646px;top:2388px">
  <div class="page">
    <div class="sec-title abs" style="left:20px;top:18px">Lesenswertes</div>
    <p class="abs" style="left:20px;top:36px;font-size:5.4px;color:var(--blue);font-weight:700;line-height:1.5">WILLENSSTÄRKE – der<br>stille Motor!</p>
    <p class="abs" style="left:20px;top:58px;font-size:5.4px;color:var(--grey);line-height:1.5">Tobi Wendler zeigt, wie<br>Sie es schaffen.</p>
    <div class="abs" style="left:0;top:128px;width:240px;height:86px;background:var(--blue)"></div>
    <div class="abs" style="left:120px;top:0;width:120px;height:343px;background:var(--slate)"></div>
    <div class="abs" role="img" aria-label="Buchcover" style="left:28px;top:110px;width:56px;height:82px;background:linear-gradient(160deg,#4a4f57,#1c2026);box-shadow:2px 3px 6px rgba(0,0,0,.3)"></div>
    <div class="sec-title abs" style="left:20px;top:240px;font-size:9.5px;line-height:1.2">Intensiv<br>Training</div>
    <p class="abs" style="left:20px;top:268px;font-size:5.4px;color:var(--blue);font-weight:700;line-height:1.5;width:90px">WEITERGEHEN! Wie Sie Ihre Ziele nachhaltig erreichen.</p>
    <p class="abs" style="left:20px;top:290px;font-size:5.4px;color:var(--grey);line-height:1.5;width:90px">Das Seminar für volle Energie und Ausdauer.</p>
    <div class="abs" style="left:132px;top:120px;width:100px">
      <div class="label" style="font-weight:600;font-size:9px;margin-bottom:10px">Interaktive<br>Vorträge</div>
      <p style="font-size:5px;color:#fff;font-weight:700;margin-bottom:3px">FOKUS! Jetzt erst recht!</p>
      <p style="font-size:5px;color:#aab2bb;line-height:1.5;margin-bottom:6px">Nicht das Anfangen wird belohnt, sondern das Durchhalten.</p>
      <div class="check"><svg width="6" height="6" viewBox="0 0 6 6"><rect x=".3" y=".3" width="5.4" height="5.4" fill="none" stroke="#aab2bb" stroke-width=".6"/><path d="M1.3 3l1.1 1.1L4.7 1.6" fill="none" stroke="#fff" stroke-width=".8"/></svg>Starten Sie mit klaren Zielen</div>
      <div class="check"><svg width="6" height="6" viewBox="0 0 6 6"><rect x=".3" y=".3" width="5.4" height="5.4" fill="none" stroke="#aab2bb" stroke-width=".6"/><path d="M1.3 3l1.1 1.1L4.7 1.6" fill="none" stroke="#fff" stroke-width=".8"/></svg>Überwinden Sie innere Hürden</div>
      <p style="font-size:5px;color:#fff;font-weight:700;margin:8px 0 6px;line-height:1.5">GLEICHKLANG! Damit alles im Lot bleibt, muss einiges verändert werden!</p>
      <div class="check"><svg width="6" height="6" viewBox="0 0 6 6"><rect x=".3" y=".3" width="5.4" height="5.4" fill="none" stroke="#aab2bb" stroke-width=".6"/><path d="M1.3 3l1.1 1.1L4.7 1.6" fill="none" stroke="#fff" stroke-width=".8"/></svg>Finden Sie Ihre innere Mitte</div>
      <div class="check"><svg width="6" height="6" viewBox="0 0 6 6"><rect x=".3" y=".3" width="5.4" height="5.4" fill="none" stroke="#aab2bb" stroke-width=".6"/><path d="M1.3 3l1.1 1.1L4.7 1.6" fill="none" stroke="#fff" stroke-width=".8"/></svg>Gewinnen Sie Kraft für den Alltag</div>
    </div>
  </div>
  <div class="page">
    <div class="abs" style="left:0;top:0;width:60px;height:343px;background:var(--slate-soft)"></div>
    <div class="han-col" style="left:16px;top:110px;color:#56616c;font-size:28px"><span>愉</span><span>快</span><span>的</span><span>春</span><span>節</span></div>
    <div class="sec-title abs" style="left:84px;top:18px">Notizen</div>
    <div class="note-line" style="left:84px;top:56px"></div>
    <div class="note-line" style="left:84px;top:88px"></div>
    <div class="note-line" style="left:84px;top:120px"></div>
    <div class="note-line" style="left:84px;top:152px"></div>
    <div class="note-line" style="left:84px;top:184px"></div>
    <div class="note-line" style="left:84px;top:216px"></div>
    <div class="note-line" style="left:84px;top:248px"></div>
    <div class="note-line" style="left:84px;top:280px"></div>
    <div class="note-line" style="left:84px;top:312px"></div>
  </div>
</section>

<!-- ===== Row 4 ===== -->
<section class="spread" style="left:59px;top:2820px">
  <div class="page">
    <div class="rule" style="left:12px;top:28px">
      <span class="rule-han">四</span><span class="rule-num">4.</span>
      <div class="rule-head"><p class="rule-lead">Bauen Sie ein</p><h3 class="rule-title">starkes Team</h3><p class="rule-lead">um sich herum!</p></div>
      <div class="rule-text"><p>Während man im Westen häufig allein kämpft, sehen sich die Menschen in Asien als Teil eines Ganzen.</p><p>Stellen Sie sich zum Erreichen Ihres Ziels ein möglichst starkes Team zusammen.</p><p>Geteiltes Leid ist halbes Leid, geteiltes Glück ist doppeltes Glück.</p><p class="note">Überlegen Sie: Wer kann Ihnen helfen und wem können Sie helfen?</p></div>
    </div>
  </div>
  <div class="page">
    <div class="rule" style="left:10px;top:28px">
      <span class="rule-han">五</span><span class="rule-num">5.</span>
      <div class="rule-head"><p class="rule-lead">Nutzen Sie die</p><h3 class="rule-title">5/25 Regel!</h3></div>
      <div class="rule-text"><p>Der erste Schritt besteht darin, 25 Dinge aufzulisten, die man erreichen möchte.</p><p>Im nächsten Schritt markieren Sie die fünf wichtigsten.</p><p>Bleibt die Frage, was mit den restlichen 20 geschieht. Ganz einfach: Sie meiden sie, bis die fünf erreicht sind.</p></div>
    </div>
  </div>
</section>

<div class="logo-sheet" style="left:700px;top:2880px;width:420px">
  <span class="logo-dot"></span>
  <span class="logo-name">TOBI WENDLER</span>
  <span class="logo-sub">KEYNOTE SPEAKER</span>
</div>

</body>
</html>
```